Quorlapex

Hi everyone!

Looks like our project is more sophisticated than we expected. So good news - we increased the budget! and one of you will sure get the prize - no money back for us!

We are a young Russian company that specializes in in-taxi entertainment. We believe that our key strength is great attention to user experience. We've devoted much effort to improve ergonomics of our devices - tablet PCs that we install in the taxis. And yes, we enjoy to simplify things!

Now we need the most basic things - a logo and some staff for client meetings (primarily advertisers and ad agencies).

As for logo - we already have one engraved on the prototypes of our device (see attached file). This is one of the ideas (still far from perfect) - what we appreciate in it is minimalistic yet stylish approach.

As for "take it to the meeting stuff" we want to start with name card, pen and notepad (A4) that we will leave in clients's office, also as a reminder. Shall your have more smart ideas - always welcome!

As for logo and name cards - we would like to make an image of serious but modern company. Our design should communicate creativity and reliability. We believe that "to understand is to simplify" - minimalistic design is the most difficult one. Its better to work hard on fonts and arrangement, than put 10 variegated images.

SO THE TASK IS TO DESIGN:
- a logo
- a name card
- a note pad (great example in attachment)
- a pen

Shall you have more questions - please ask in comments.

We look forward to meeting like-minded fellows here!

Target Market(s)

Out target are:

- advertiser
- advertising agencies
- taxi passenger

Industry/Entity Type

It Company

Requirements
Must have
• font should be chosen very carefully
Nice to have
• classic minimalistic plain text only but very stylish name card is a dream of one of our co-founders:)
Should not have
• we do not want to have taxi-like colors and chess-boards. We are closer to "innovation", "entertainment", and "user experience", rather than "taxi".

```html
<!DOCTYPE html>
<html lang="en">
<head>
<meta charset="utf-8">
<title>Quorlapex — Notepad A4</title>
<link rel="stylesheet" href="https://fonts.googleapis.com/css2?family=Open+Sans:wght@300;400&display=swap">
<style>
  :root {
    --canvas-bg: #ffffff;
    --sheet-bg: #ffffff;
    --sheet-edge: #e6e8ea;
    --brand-blue: #4e6f88;
    --grid-line: #e1e4e7;
    --rule-grey: #b9c4cd;
  }
  html, body {
    margin: 0;
    padding: 0;
    width: 1200px;
    height: 1000px;
    overflow: hidden;
    background: var(--canvas-bg);
  }
  .notepad-sheet {
    position: absolute;
    left: 280px;
    top: 48px;
    width: 638px;
    height: 902px;
    background: var(--sheet-bg);
    border: 1px solid var(--sheet-edge);
    box-sizing: border-box;
  }
  .brand-name {
    position: absolute;
    left: 30px;
    top: 22px;
    margin: 0;
    font-family: "Open Sans", sans-serif;
    font-weight: 300;
    font-size: 50px;
    line-height: 1;
    letter-spacing: 0.5px;
    color: var(--brand-blue);
  }
  .writing-grid {
    position: absolute;
    left: 30px;
    top: 119px;
    width: 580px;
    height: 742px;
  }
  .contact-block {
    position: absolute;
    left: 108px;
    top: 843px;
    padding: 1px 0 1px 9px;
    border-left: 2px solid var(--rule-grey);
    background: var(--sheet-bg);
    font-family: "Open Sans", sans-serif;
    font-weight: 400;
    font-size: 9.5px;
    line-height: 10px;
    color: var(--brand-blue);
  }
  .contact-block p { margin: 0; }
</style>
</head>
<body>
  <main class="notepad-sheet">
    <h1 class="brand-name">quorlapex</h1>

    <svg class="writing-grid" viewBox="0 0 580 742" aria-hidden="true">
      <defs>
        <pattern id="grid-cell" width="25.1" height="25.1" patternUnits="userSpaceOnUse">
          <path d="M0 0.5H25.1 M0.5 0V25.1" fill="none" stroke="var(--grid-line)" stroke-width="1" stroke-dasharray="5 4"/>
        </pattern>
      </defs>
      <rect x="0" y="0" width="580" height="742" fill="url(#grid-cell)"/>
    </svg>

    <address class="contact-block">
      <p class="contact-phone">+7 55512840</p>
      <p class="contact-email">quorlapex@quorlapex.com</p>
      <p class="contact-web">www.quorlapex.com</p>
    </address>
  </main>
</body>
</html>
```